helping new make my new business shine, with your design for : Vellaroque Fashions

Create business card for Vellaroque Fashions,( which means to shine in French)
I'm starting up a new online retail clothing store. My main voice is to sell outfit for Church and church events for men and women. (But geared more towards women)
1. photos included are from a catolog of the clothes that will be on my web site
2. Create your owns look keeping my example in mind.
3 . I want small articles of clothing on the card a few dresses, some pants, men suit
women hats, one in each corner of the card., sunglasses.all these articles are to be placed on the front of my business card to show my inventory. I want people to look at my business card and want to check out my web site.
Place each of these written out in different areas on the card clergy robes, usher uniforms, egyptian linen, men's accessories. sunglasses
4. Make your article of clothing BLING I like things that sparkle
5. On the back side will be all the contact information. The letters are to be in English or Script if you can make the business name lettering in 3D would be great but not nessassary.
Vellaroque Fashions
Order online 24/7 at: vellaroquefashions.com
Bus/Fax 505-731-6642
Mon-Wed 8:00am till 12:00 pm mst.
Lorna Whitby, Owner
lornawhitby45@quillpost.net

I'm looking forward to receiving some outstanding designs. I known the space your working with is small but when creating the women's attire and hats make them bling where possible more is better as long as it's elegant. Thank you Added Sunday, August 7, 2016

Christains women& men who take pride in what they wear to church, and who just want to look good at any high dollar event without having to spent a lot.

Fashion

The words need to be jumping out at you (3D lettering,) but ONLY if they can be done elegantly,
Vellaroque Fashions
Order online at: vellaroquefashion.com
505-731-6643
Lorna Whitby, CEO
All the contact information to be placed on the backside

Decorative
Script

• Everything I stated in the project description.
• Bling on the women attire photos and hats
• -Ok to use the photos that are attached in your business card submission (please refrain from using the model's faces, only the clothing)
• -I do not have logo but please just use the business name is a creative way
• Everything's indicated
• 1. The drawings should not use my photos but create a new look.
• 2. Do Not Use a black backing

```html
<!DOCTYPE html>
<html lang="en">
<head>
<meta charset="utf-8">
<title>Vellaroque Fashions — Business Card</title>
<link rel="stylesheet" href="https://fonts.googleapis.com/css2?family=Great+Vibes&family=Noto+Serif:ital,wght@1,400&display=swap">
<style>
  :root {
    --backdrop: #efe9e2;
    --card: #ffffff;
    --ink: #121212;
    --sparkle: #b9b9b9;
    --sparkle-light: #dcdcdc;
    --silhouette: #7a7a7a;
    --shadow: rgba(60, 45, 30, 0.18);
  }
  * { box-sizing: border-box; margin: 0; padding: 0; }
  html, body {
    width: 1074px;
    height: 1200px;
    overflow: hidden;
    background: var(--backdrop);
  }
  .canvas {
    position: relative;
    width: 1074px;
    height: 1200px;
  }
  .card {
    position: absolute;
    left: 107px;
    width: 835px;
    height: 470px;
    background: var(--card);
    box-shadow: 6px 8px 0 var(--shadow);
  }
  .card--front { top: 109px; }
  .card--back  { top: 632px; }

  .script {
    font-family: "Great Vibes", cursive;
    color: var(--ink);
    white-space: nowrap;
  }
  .category {
    position: absolute;
    font-size: 45px;
    line-height: 1;
    transform-origin: left center;
  }
  .category--accessories { left: 14px;  top: 30px;  transform: rotate(-8deg); }
  .category--ushers      { left: 630px; top: 30px;  transform: rotate(-8deg); }
  .category--sunglasses  { left: 690px; top: 258px; transform: rotate(-12deg); }
  .category--robes       { left: 10px;  top: 316px; transform: rotate(38deg); }
  .category--linen       { left: 398px; top: 400px; transform: rotate(4deg); }

  .item {
    position: absolute;
    background: linear-gradient(160deg, var(--sparkle-light), var(--sparkle) 55%, #9d9d9d);
    border-radius: 6px;
  }
  .item--sheath-dress  { left: 257px; top: 17px;  width: 44px;  height: 110px; border-radius: 14px 14px 6px 6px; }
  .item--bow-tie       { left: 565px; top: 23px;  width: 57px;  height: 31px; }
  .item--necktie       { left: 13px;  top: 139px; width: 31px;  height: 104px; border-radius: 4px 4px 14px 14px; }
  .item--sunglasses    { left: 715px; top: 187px; width: 105px; height: 45px; border-radius: 10px 10px 20px 20px; }
  .item--shirt         { left: 235px; top: 376px; width: 51px;  height: 77px; }
  .item--flared-dress  { left: 658px; top: 330px; width: 77px;  height: 130px; border-radius: 12px 12px 4px 4px; }

  .brand {
    position: absolute;
    left: 155px;
    top: 150px;
    width: 568px;
    text-align: center;
    font-size: 78px;
    font-weight: 400;
    line-height: 1;
  }
  .brand-rule {
    position: absolute;
    left: 155px;
    top: 245px;
    width: 568px;
    height: 4px;
    background: var(--ink);
  }

  .contact {
    position: absolute;
    left: 57px;
    top: 96px;
  }
  .contact__name {
    font-size: 51px;
    line-height: 50px;
  }
  .contact__line {
    font-family: "Noto Serif", Georgia, serif;
    font-style: italic;
    font-size: 31px;
    line-height: 36.5px;
    color: var(--ink);
    white-space: nowrap;
  }
  .wardrobe {
    position: absolute;
    left: 68px;
    top: 352px;
    display: flex;
    gap: 18px;
  }
  .wardrobe__piece {
    width: 75px;
    height: 107px;
    background: var(--silhouette);
  }
  .wardrobe__piece--suit   { border-radius: 8px 8px 2px 2px; }
  .wardrobe__piece--jacket { border-radius: 10px 10px 2px 2px; }
  .wardrobe__piece--dress  { width: 60px; height: 96px; margin-top: 6px; border-radius: 10px 10px 4px 4px; }
  .wardrobe__piece--gown   { width: 66px; height: 102px; margin-top: 2px; border-radius: 12px 12px 4px 4px; }
</style>
</head>
<body>
<main class="canvas">

  <section class="card card--front" aria-label="Business card front">
    <span class="script category category--accessories">men's accesories</span>
    <span class="script category category--ushers">usher uniforms</span>
    <span class="script category category--sunglasses">sunglasses</span>
    <span class="script category category--robes">clergy robes</span>
    <span class="script category category--linen">egyptian linen</span>

    <div class="item item--sheath-dress" role="img" aria-label="Sparkling silver sheath dress"></div>
    <div class="item item--bow-tie" role="img" aria-label="Sparkling silver bow tie"></div>
    <div class="item item--necktie" role="img" aria-label="Sparkling silver necktie"></div>
    <div class="item item--sunglasses" role="img" aria-label="Sparkling silver aviator sunglasses"></div>
    <div class="item item--shirt" role="img" aria-label="Sparkling silver dress shirt"></div>
    <div class="item item--flared-dress" role="img" aria-label="Sparkling silver flared dress"></div>

    <h1 class="script brand">Vellaroque Fashion</h1>
    <div class="brand-rule"></div>
  </section>

  <section class="card card--back" aria-label="Business card back">
    <div class="contact">
      <p class="script contact__name">Vellaroque Fashions</p>
      <p class="contact__line">Order online 24/7 at: vellaroquefashions.com</p>
      <p class="contact__line">Bus/Fax 505-731-6642</p>
      <p class="contact__line">Mon-Wed 8:00am till 12:00 pm mst.</p>
      <p class="contact__line">Lorna Whitby, Owner</p>
      <p class="contact__line">lornawhitby45@quillpost.net</p>
    </div>
    <div class="wardrobe">
      <div class="wardrobe__piece wardrobe__piece--suit" role="img" aria-label="Grey men's suit silhouette"></div>
      <div class="wardrobe__piece wardrobe__piece--jacket" role="img" aria-label="Grey suit jacket silhouette"></div>
      <div class="wardrobe__piece wardrobe__piece--dress" role="img" aria-label="Grey belted dress silhouette"></div>
      <div class="wardrobe__piece wardrobe__piece--gown" role="img" aria-label="Grey flared gown silhouette"></div>
    </div>
  </section>

</main>
</body>
</html>
```